In-Aisle Customer Special Order Process and FAQ

This infographic/brochure is intended for owners of Birchwell Supply retail stores who I'm looking to inform about a new process for managing customer special orders. There will be two pages to this infographic / FAQ.

The first page I am looking for a very unique and creative way to educate them on the steps needed to process a customer special order. The two PowerPoint slides I attached is the content for this process. I'm looking to illustrate this information in a very fun and differentiated way that will catch the Birchwell Supply owners' attention! It must stand out. Right now, the way that it is laid out is boring, unattractive to look at, and too cluttered. I will need all this content, but it will need to be formatted and designed in a much, much better way. Note that step 7 could be either an in-store pick-up or deliver (not both), so the infographic must make that clear.

* Use logos provided. The red vest logo is the mobile app

The second page is a frequently asked question section. This should be in a two column form and match the design of the first page.

Feel free to use some of the images I provided, but not necessary.

Target Market(s)

Birchwell Supply Store Owners

Font styles to use
Serif

Colors
EB3D1F
EC4F4E
F09395
F8D3D4
FCEDEE

Requirements
Must have
• Birchwell Supply red and black colors; 8-1/2x11; 2 pages, front and back, Super creative, different looking, eye catching, use all the content I provided. Must include each step, system touchpoints, Lead/location, actions, and outcomes; size 11 font or bigger
Nice to have
• Some of the photos I sent

```html
<!DOCTYPE html>
<html lang="en">
<head>
<meta charset="utf-8">
<title>In-Aisle Customer Special Order Process</title>
<link href="https://fonts.googleapis.com/css2?family=Playfair+Display:wght@700&family=Source+Sans+3:wght@400;600;700&display=swap" rel="stylesheet">
<style>
:root{
  --red:#eb3d1f;
  --red-deep:#d7262c;
  --ink:#1f1d1e;
  --ink-soft:#2b2829;
  --text:#d9d6d6;
  --muted:#9c9898;
  --white:#ffffff;
  --backdrop:#cfe4ea;
  --q-blue:#3f9be0;
  --s1:#eb3d1f;--s2:#f26522;--s3:#d6247a;--s4:#5b3a96;--s5:#1e88c8;--s6:#1fa9a0;--s7:#7dbb42;
}
*{box-sizing:border-box;margin:0;padding:0}
html,body{width:1200px;height:3900px;overflow:hidden}
body{background:var(--backdrop);font-family:"Source Sans 3",Arial,sans-serif;position:relative;color:var(--text)}
.page{position:absolute;left:150px;width:900px;height:1240px;background:var(--ink);overflow:hidden;box-shadow:0 4px 18px rgba(0,0,0,.18)}
.page--process{top:40px}
.page--faq-a{top:1330px}
.page--faq-b{top:2620px}
.serif{font-family:"Playfair Display",Georgia,serif}

/* process header */
.process-header{position:absolute;left:0;top:0;width:900px;height:330px;background:var(--white)}
.photo{position:absolute;background:linear-gradient(120deg,#6b5a4e,#a8927c 40%,#3b2f2c 75%,#8a2a22)}
.process-header .photo{left:360px;top:0;width:540px;height:330px}
.header-band{position:absolute;left:0;top:0;width:560px;height:330px}
.brand{position:absolute;left:36px;top:22px;display:flex;align-items:center;gap:10px;color:var(--white)}
.brand__mark{width:14px;height:14px;background:var(--white)}
.brand__name{font-weight:700;font-size:20px;letter-spacing:.5px}
.brand__sub{font-weight:600;font-size:11px;letter-spacing:1.5px;line-height:1.2}
.process-title{position:absolute;left:36px;top:120px;width:360px;color:var(--white);font-size:42px;line-height:1.12}

/* steps */
.step{position:absolute;width:205px;font-size:11px;line-height:1.45}
.step h3{font-family:"Playfair Display",Georgia,serif;color:var(--white);font-size:17px;margin-bottom:8px}
.step .label{color:var(--white);font-weight:700}
.step ul{margin:4px 0 6px 14px}
.step p{margin-bottom:4px}
.steps-top .step{top:356px}
.steps-bottom .step{top:800px}
.markers{position:absolute;left:0;top:640px}
.marker-num{font-family:"Playfair Display",Georgia,serif;font-size:20px;font-weight:700;fill:var(--white)}
.process-footer{position:absolute;left:0;bottom:0;width:900px;height:70px;background:var(--red);display:flex;align-items:center;padding:0 30px;color:var(--white)}
.process-footer .misc{font-family:"Playfair Display",Georgia,serif;font-size:20px;background:var(--red-deep);padding:8px 18px;margin-left:-30px;height:70px;display:flex;align-items:center}
.process-footer .contact{font-size:12px;margin-left:140px}
.net-name{font-weight:700;font-size:22px;color:var(--white);margin-left:auto}

/* faq */
.faq-hero{position:absolute;left:0;top:0;width:900px;height:470px}
.faq-hero .photo{left:0;top:0;width:900px;height:470px;background:linear-gradient(90deg,#5a4a40,#8c7563 35%,#3a2c28 60%,#7a2e26 80%,#2e2523)}
.faq-hero .shade{position:absolute;left:0;top:0;width:900px;height:470px;background:linear-gradient(180deg,rgba(31,29,30,0) 40%,rgba(31,29,30,.85) 90%,var(--ink))}
.faq-title{position:absolute;left:0;top:375px;width:900px;text-align:center;color:var(--white);font-size:40px}
.faq-cols{position:absolute;left:40px;top:490px;width:820px;display:grid;grid-template-columns:1fr 1fr;column-gap:40px;row-gap:26px}
.faq-item{display:flex;gap:10px;font-size:11px;line-height:1.45}
.faq-num{flex:0 0 20px;height:20px;border-radius:50%;background:var(--red);color:var(--white);font-size:11px;font-weight:700;display:flex;align-items:center;justify-content:center}
.faq-q{color:var(--white);font-weight:700;font-size:12px;margin-bottom:6px}
.page--faq-b .faq-q{color:var(--q-blue)}
.page--faq-b .faq-num{background:var(--q-blue)}
.faq-a{color:var(--muted)}
.faq-footer{position:absolute;left:0;bottom:0;width:900px;height:60px;display:flex;align-items:center;padding:0 30px;gap:40px;font-size:12px}
.page--faq-a .faq-footer{background:var(--white);color:var(--ink)}
.page--faq-a .faq-footer .net-name{color:var(--red)}
.page--faq-b .faq-footer{background:var(--red);color:var(--white)}
.footer-brand{font-weight:700;font-size:18px}
.page--faq-a .footer-brand{color:var(--red)}
.contact-line{display:flex;align-items:center;gap:6px}
.socials{display:flex;gap:8px;margin-left:auto}
.socials span{width:22px;height:22px;border-radius:50%;background:var(--white)}
</style>
</head>
<body>

<section class="page page--process">
  <header class="process-header">
    <div class="photo" role="img" aria-label="Photo of a store associate helping a customer in an aisle"></div>
    <svg class="header-band" viewBox="0 0 560 330" aria-hidden="true"><polygon points="0,0 560,0 380,330 0,330" fill="#eb3d1f"/></svg>
    <div class="brand"><span class="brand__mark"></span><span class="brand__name">Birchwell Supply</span><span class="brand__sub">STORE SYSTEMS &amp;<br>OPERATIONS</span></div>
    <h1 class="process-title serif">In-Aisle Customer Special Order Process</h1>
  </header>

  <div class="steps-top">
    <div class="step" style="left:30px">
      <h3>Order Entry</h3>
      <p><span class="label">System Touchpoint:</span> Mobile app in-aisle order screen</p>
      <p><span class="label">Lead / Location:</span> Sales associate, in the aisle</p>
      <p class="label">Actions:</p>
      <ul><li>Look up the item and vendor</li><li>Enter customer name and phone</li><li>Confirm price and quantity</li><li>Choose pick-up or delivery</li></ul>
      <p class="label">Outcomes:</p>
      <ul><li>Special order created and saved</li></ul>
    </div>
    <div class="step" style="left:250px">
      <h3>Receive</h3>
      <p><span class="label">System Touchpoint:</span> Receiving screen</p>
      <p><span class="label">Lead / Location:</span> Receiving team, back room</p>
      <p class="label">Actions:</p>
      <ul><li>Match item to the open order</li><li>Check for damage</li><li>Tag with customer name</li></ul>
      <p class="label">Outcomes:</p>
      <ul><li>Order marked as received</li></ul>
    </div>
    <div class="step" style="left:465px">
      <h3>Ship</h3>
      <p><span class="label">System Touchpoint:</span> Vendor portal</p>
      <p><span class="label">Lead / Location:</span> Vendor or distribution center</p>
      <p class="label">Actions:</p>
      <ul><li>Vendor confirms and ships</li><li>Tracking number is posted</li></ul>
      <p class="label">Outcomes:</p>
      <ul><li>Store sees expected arrival date</li></ul>
    </div>
    <div class="step" style="left:680px">
      <h3>In-Store Pick Up or Deliver</h3>
      <p><span class="label">System Touchpoint:</span> Point of sale</p>
      <p><span class="label">Lead / Location:</span> Front counter or driver</p>
      <p class="label">Pick Up (one option):</p>
      <ul><li>Call customer, hold at counter</li><li>Close order at the register</li></ul>
      <p class="label">Deliver (other option):</p>
      <ul><li>Schedule route and drop off</li></ul>
      <p class="label">Outcomes:</p>
      <ul><li>Order complete, customer notified</li></ul>
    </div>
  </div>

  <svg class="markers" width="900" height="140" viewBox="0 0 900 140" aria-hidden="true">
    <g>
      <polygon points="78,10 178,10 178,50 128,74 78,50" fill="#eb3d1f"/><text class="marker-num" x="128" y="44" text-anchor="middle">01</text>
      <polygon points="300,10 400,10 400,50 350,74 300,50" fill="#d6247a"/><text class="marker-num" x="350" y="44" text-anchor="middle">03</text>
      <polygon points="512,10 612,10 612,50 562,74 512,50" fill="#1e88c8"/><text class="marker-num" x="562" y="44" text-anchor="middle">05</text>
      <polygon points="730,10 830,10 830,50 780,74 730,50" fill="#7dbb42"/><text class="marker-num" x="780" y="44" text-anchor="middle">07</text>
      <polygon points="180,120 280,120 280,80 230,56 180,80" fill="#f26522"/><text class="marker-num" x="230" y="110" text-anchor="middle">02</text>
      <polygon points="400,120 500,120 500,80 450,56 400,80" fill="#5b3a96"/><text class="marker-num" x="450" y="110" text-anchor="middle">04</text>
      <polygon points="620,120 720,120 720,80 670,56 620,80" fill="#1fa9a0"/><text class="marker-num" x="670" y="110" text-anchor="middle">06</text>
    </g>
  </svg>

  <div class="steps-bottom">
    <div class="step" style="left:130px">
      <h3>Complete PO/Tax</h3>
      <p><span class="label">System Touchpoint:</span> Purchase order screen</p>
      <p><span class="label">Lead / Location:</span> Sales associate, register</p>
      <p class="label">Actions:</p>
      <ul><li>Collect deposit or full payment</li><li>Apply tax rules</li><li>Print customer receipt</li></ul>
      <p class="label">Outcomes:</p>
      <ul><li>Purchase order is released</li></ul>
    </div>
    <div class="step" style="left:350px">
      <h3>Review</h3>
      <p><span class="label">System Touchpoint:</span> Order dashboard</p>
      <p><span class="label">Lead / Location:</span> Store manager, office</p>
      <p class="label">Actions:</p>
      <ul><li>Approve open orders daily</li><li>Fix any missing details</li></ul>
      <p class="label">Outcomes:</p>
      <ul><li>Order sent to the vendor</li></ul>
    </div>
    <div class="step" style="left:570px">
      <h3>Availability</h3>
      <p><span class="label">System Touchpoint:</span> Order status view</p>
      <p><span class="label">Lead / Location:</span> Store manager, office</p>
      <p class="label">Actions:</p>
      <ul><li>Check stock and lead time</li><li>Update the customer on timing</li></ul>
      <p class="label">Outcomes:</p>
      <ul><li>Customer knows the ship date</li></ul>
    </div>
  </div>

  <footer class="process-footer">
    <span class="misc">Miscellaneous</span>
    <span class="contact">Contact: Store Operations Support Office</span>
    <span class="net-name">Birchwell Net</span>
  </footer>
</section>

<section class="page page--faq-a">
  <div class="faq-hero">
    <div class="photo" role="img" aria-label="Photo of a customer talking with a store associate"></div>
    <div class="shade"></div>
    <h2 class="faq-title serif">Frequently Asked Questions</h2>
  </div>
  <div class="faq-cols">
    <div class="faq-item"><span class="faq-num">1</span><div><p class="faq-q">What is needed to start an in-aisle special order?</p><p class="faq-a">Only the mobile app and the customer's name and phone number. The item can be found by keyword, vendor code or scan, and the order is saved right in the aisle.</p></div></div>
    <div class="faq-item"><span class="faq-num">6</span><div><p class="faq-q">Can a customer change an order after it is placed?</p><p class="faq-a">Yes, until the manager review is done. After the order goes to the vendor, changes need a new order and the old one is closed.</p></div></div>
    <div class="faq-item"><span class="faq-num">2</span><div><p class="faq-q">How is the deposit handled at checkout?</p><p class="faq-a">The register shows the open order. Take the deposit or full payment, apply tax, and hand the customer a printed receipt with the order number.</p></div></div>
    <div class="faq-item"><span class="faq-num">7</span><div><p class="faq-q">What happens if the vendor is out of stock?</p><p class="faq-a">The status view flags the item. Call the customer with a new date or offer a similar item from another vendor.</p></div></div>
    <div class="faq-item"><span class="faq-num">3</span><div><p class="faq-q">Who reviews open orders each day?</p><p class="faq-a">The store manager or a chosen lead checks the dashboard each morning and approves orders so they reach the vendor the same day.</p></div></div>
    <div class="faq-item"><span class="faq-num">8</span><div><p class="faq-q">Can one order be both picked up and delivered?</p><p class="faq-a">No. Each order uses one option only, chosen at order entry. It can be switched before the item arrives.</p></div></div>
    <div class="faq-item"><span class="faq-num">4</span><div><p class="faq-q">How will the customer know the item has arrived?</p><p class="faq-a">Once received, the system sends a text, and the store can also call. Items are held at the counter for fourteen days.</p></div></div>
    <div class="faq-item"><span class="faq-num">9</span><div><p class="faq-q">Where do I get help with the new process?</p><p class="faq-a">Reach the Store Operations support team by phone or email, listed below, during regular business hours.</p></div></div>
    <div class="faq-item"><span class="faq-num">5</span><div><p class="faq-q">What reports track special orders?</p><p class="faq-a">The dashboard lists open, late and closed orders, and can be printed or sent by email each week.</p></div></div>
  </div>
  <footer class="faq-footer">
    <span class="footer-brand">Birchwell Supply</span>
    <span class="contact-line"><svg width="12" height="12" viewBox="0 0 24 24" aria-hidden="true"><path d="M6.6 10.8a15 15 0 006.6 6.6l2.2-2.2a1 1 0 011-.25 11 11 0 003.5.56 1 1 0 011 1V20a1 1 0 01-1 1A17 17 0 013 4a1 1 0 011-1h3.5a1 1 0 011 1 11 11 0 00.56 3.5 1 1 0 01-.25 1z" fill="#eb3d1f"/></svg>1-800-555-0184</span>
    <span class="contact-line">orders@birchwellsupply.example</span>
    <span class="net-name">Birchwell Net</span>
  </footer>
</section>

<section class="page page--faq-b">
  <div class="faq-hero">
    <div class="photo" role="img" aria-label="Photo of a customer talking with a store associate"></div>
    <div class="shade"></div>
    <h2 class="faq-title serif">Frequently Asked Questions</h2>
  </div>
  <div class="faq-cols">
    <div class="faq-item"><span class="faq-num">1</span><div><p class="faq-q">What is needed to start an in-aisle special order?</p><p class="faq-a">Only the mobile app and the customer's name and phone number. The item can be found by keyword, vendor code or scan, and the order is saved right in the aisle.</p></div></div>
    <div class="faq-item"><span class="faq-num">6</span><div><p class="faq-q">Can a customer change an order after it is placed?</p><p class="faq-a">Yes, until the manager review is done. After the order goes to the vendor, changes need a new order and the old one is closed.</p></div></div>
    <div class="faq-item"><span class="faq-num">2</span><div><p class="faq-q">How is the deposit handled at checkout?</p><p class="faq-a">The register shows the open order. Take the deposit or full payment, apply tax, and hand the customer a printed receipt with the order number.</p></div></div>
    <div class="faq-item"><span class="faq-num">7</span><div><p class="faq-q">What happens if the vendor is out of stock?</p><p class="faq-a">The status view flags the item. Call the customer with a new date or offer a similar item from another vendor.</p></div></div>
    <div class="faq-item"><span class="faq-num">3</span><div><p class="faq-q">Who reviews open orders each day?</p><p class="faq-a">The store manager or a chosen lead checks the dashboard each morning and approves orders so they reach the vendor the same day.</p></div></div>
    <div class="faq-item"><span class="faq-num">8</span><div><p class="faq-q">Can one order be both picked up and delivered?</p><p class="faq-a">No. Each order uses one option only, chosen at order entry. It can be switched before the item arrives.</p></div></div>
    <div class="faq-item"><span class="faq-num">4</span><div><p class="faq-q">How will the customer know the item has arrived?</p><p class="faq-a">Once received, the system sends a text, and the store can also call. Items are held at the counter for fourteen days.</p></div></div>
    <div class="faq-item"><span class="faq-num">9</span><div><p class="faq-q">Where do I get help with the new process?</p><p class="faq-a">Reach the Store Operations support team by phone or email, listed below, during regular business hours.</p></div></div>
    <div class="faq-item"><span class="faq-num">5</span><div><p class="faq-q">What reports track special orders?</p><p class="faq-a">The dashboard lists open, late and closed orders, and can be printed or sent by email each week.</p></div></div>
  </div>
  <footer class="faq-footer">
    <span class="footer-brand">Birchwell Net</span>
    <span class="contact-line"><svg width="12" height="12" viewBox="0 0 24 24" aria-hidden="true"><path d="M6.6 10.8a15 15 0 006.6 6.6l2.2-2.2a1 1 0 011-.25 11 11 0 003.5.56 1 1 0 011 1V20a1 1 0 01-1 1A17 17 0 013 4a1 1 0 011-1h3.5a1 1 0 011 1 11 11 0 00.56 3.5 1 1 0 01-.25 1z" fill="#ffffff"/></svg>1-800-555-0184</span>
    <span class="contact-line">orders@birchwellsupply.example</span>
    <span class="socials"><span></span><span></span><span></span></span>
  </footer>
</section>

</body>
</html>
```